Modern luxury trendy cosmetics label

Looking for a cosmetics packaging label design. We are looking for a professionel, modern and luxury look like Helena Voskuijl, Meadowfern Apothecary, Autumn Vale, Gordon Ellis Marsh, Quba, Oskar + Brandt, Velumo, Dizzy Walrus, the plainspoken, lumires de charme.Name of product: Alpine Edelweiss Wrap - No-Needle Contour Treatment Ingredients that have scientific proof of anti aging: Cherry blossom extact, collegen, hyaluronic acid, coconut oil. Color of product itself: Pastel pink. Smell: Cherry blossom. Colors of label: simple and black and white or some subtle colors.

Target Market(s)

Women, luxury market, modern women, young and old women

Industry/Entity Type

Cosmetics

Font styles to use
Sans Serif

Colors

Designer to choose colors to be used in the design.

Requirements
Must have
• A modern look, professional, cosmetics, beauty, professional market, original

```html
<!DOCTYPE html>
<html lang="en">
<head>
<meta charset="utf-8">
<title>Ovela – Alpine Edelweiss Wrap labels</title>
<link rel="stylesheet" href="https://fonts.googleapis.com/css2?family=Cinzel:wght@400&family=Montserrat:wght@400;500;600;700&display=swap">
<style>
  :root {
    --bg: #ffffff;
    --ink: #141414;
    --ink-soft: #5a5a5a;
    --silver-light: #e4e4e4;
    --silver-mid: #c9c9c9;
    --silver-dark: #b5b5b5;
    --bar: #1b1b1b;
    --bar-text: #ffffff;
  }
  * { margin: 0; padding: 0; box-sizing: border-box; }
  html, body {
    width: 1200px; height: 712px; overflow: hidden;
    background: var(--bg);
    font-family: "Montserrat", sans-serif;
    color: var(--ink);
  }
  .canvas { position: relative; width: 1200px; height: 712px; }
  .label {
    position: absolute;
    top: 262px;
    height: 372px;
    background: linear-gradient(90deg, var(--silver-dark) 0%, var(--silver-light) 30%, var(--silver-mid) 60%, var(--silver-light) 85%, var(--silver-dark) 100%);
  }
  .label--centered { left: 118px; width: 404px; text-align: center; }
  .label--vertical { left: 648px; width: 456px; }

  /* centred label */
  .brand { font-family: "Montserrat", sans-serif; font-weight: 400; color: var(--ink); letter-spacing: -1px; }
  .label--centered .brand { position: absolute; left: 0; right: 0; top: 20px; font-size: 72px; line-height: 1; }
  .label--centered .product-name {
    position: absolute; left: 0; right: 0; top: 116px;
    font-family: "Cinzel", serif; font-size: 29px; line-height: 1.25; color: var(--ink);
  }
  .claim-bar {
    position: absolute; left: 28px; right: 28px; top: 240px; height: 32px;
    background: var(--bar); color: var(--bar-text);
    font-size: 15px; font-weight: 600; letter-spacing: 0.3px; line-height: 32px;
  }
  .label--centered .ingredients-note { position: absolute; left: 0; right: 0; top: 306px; }

  .ingredients-intro { font-size: 10px; color: var(--ink-soft); line-height: 1.4; }
  .ingredients-list { font-size: 14px; font-weight: 600; line-height: 1.35; color: var(--ink); }

  /* vertical label */
  .label--vertical .brand {
    position: absolute; left: 20px; top: 340px;
    font-size: 132px; line-height: 1;
    transform-origin: 0 0; transform: rotate(-90deg);
    white-space: nowrap;
  }
  .label--vertical .text-column { position: absolute; left: 194px; top: 54px; right: 10px; }
  .label--vertical .product-name { font-weight: 500; line-height: 1.1; letter-spacing: 1px; }
  .product-name__line1 { font-size: 32px; display: block; }
  .product-name__line2 { font-size: 23px; display: block; margin-top: 4px; }
  .label--vertical .claim { margin-top: 44px; font-size: 15px; font-weight: 700; line-height: 1.4; letter-spacing: 0.3px; }
  .label--vertical .ingredients-note { margin-top: 52px; }
</style>
</head>
<body>
<main class="canvas">
  <section class="label label--centered" aria-label="Label, centred layout">
    <div class="brand">ovela</div>
    <h1 class="product-name">Alpine Edelweiss<br>Wrap</h1>
    <div class="claim-bar">NO-NEEDLE CONTOUR TREATMENT</div>
    <div class="ingredients-note">
      <p class="ingredients-intro">Ingredients that have Scientific Proof of Anti Aging:</p>
      <p class="ingredients-list">Cherry blossom extact, Collegen,<br>Hyaluronic Acid, Coconut Oil.</p>
    </div>
  </section>

  <section class="label label--vertical" aria-label="Label, vertical brand layout">
    <div class="brand">ovela</div>
    <div class="text-column">
      <h2 class="product-name">
        <span class="product-name__line1">ALPINE</span>
        <span class="product-name__line2">EDELWEISS WRAP</span>
      </h2>
      <p class="claim">NO-NEEDLE<br>CONTOUR TREATMENT</p>
      <div class="ingredients-note">
        <p class="ingredients-intro">Ingredients that have Scientific<br>Proof of Anti Aging:</p>
        <p class="ingredients-list">Cherry blossom extact,<br>Collegen, Hyaluronic Acid,<br>Coconut Oil.</p>
      </div>
    </div>
  </section>
</main>
</body>
</html>
```